Political sign design, fonts colors and layout

I am running for Town Council.

My message is done, and *a draft is attached* with the text we wish to use. It says "Elect Dana Velloway" etc. In Maroon and White. I am not a designer, but this is somewhat close to what we are looking for.

I need help with colors and fonts, layout, spacing, and general cleanup.

I'm attaching the town high school logo:

- "B" for Brockmere: with black and white outlines on the fonts
- we want to incorporate the black and white on the fonts
- for the entire text, parts of the text, or best would be a mix

This is for signs printed and placed all over my town.

We need two versions

1. square, 4' by 4' version
2. 36" by 24" version

The smaller version will drop the three bullet pointed text, but otherwise can be identical.

The sign can only use 3 printed colors (due to printing costs.)

1. maroon,
2. white,
3. black.

The maroon should match the maroon from the high school logo attached, which I believe I did in the draft.

We also like the white border around the outside, like in the "scoreboard" design attached.

Thanks for your attention, wish me luck.

Dana

Target Market(s)

SIgns, Political market

Industry/Entity Type

Political

Font styles to use
Sans Serif
Other font styles liked:
• Arial Black, Sans Serif Bold

Requirements
Must have
• maroon background, white font.
• - black borders around fonts where appropriate
• - great spacing
• - great typeface usage
• - clean and crisp political sign, visible while driving.
• - my name "Dana Velloway" much larger like the draft, or the appropriate additional size
• - two versions, one square, and one 36" / 24"
Nice to have
• - nice borders
• - dress it up a bit, using italics and bold fonts, without making it flashy or busy.
Should not have
• Must be easily readable from a car, except for "Paid for by Friends of Dana Velloway" which can be tiny.
• Colors are noted in the description, the "Brockmere Maroon" as the background, white font, and some use of black.

```html
<!DOCTYPE html>
<html lang="en">
<head>
<meta charset="utf-8">
<title>Elect Dana Velloway – Yard Signs</title>
<link rel="stylesheet" href="https://fonts.googleapis.com/css2?family=Josefin+Sans:ital,wght@0,400;0,600;1,300;1,400&family=Open+Sans:ital,wght@0,400;0,800;1,400;1,800&display=swap">
<style>
  :root{
    --page:#000;
    --maroon:#7a1c22;
    --white:#fff;
    --black:#000;
  }
  *{margin:0;padding:0;box-sizing:border-box}
  html,body{width:801px;height:1200px;overflow:hidden;background:var(--page)}
  .canvas{position:relative;width:801px;height:1200px}

  .sign{position:absolute;background:var(--maroon);overflow:hidden}
  .sign::before,.sign::after{content:"";position:absolute;border:2px solid var(--white)}
  .sign::before{inset:7px}
  .sign::after{inset:12px;border-width:1px;border-color:var(--black)}

  .sign--square{left:19px;top:19px;width:764px;height:761px}
  .sign--wide{left:115px;top:801px;width:570px;height:382px}

  .line{position:absolute;left:0;right:0;text-align:center;white-space:nowrap;color:var(--white)}
  .outlined{-webkit-text-stroke:4px var(--black);paint-order:stroke fill}
  .shadowed{text-shadow:2px 2px 0 var(--black)}

  .slogan{font-family:"Josefin Sans",sans-serif;font-weight:600}
  .ballot{font-family:"Josefin Sans",sans-serif;font-weight:400;font-style:italic}
  .web{font-family:"Josefin Sans",sans-serif;font-weight:600}

  .name-row{display:flex;justify-content:center;align-items:flex-end}
  .elect{font-family:"Open Sans",sans-serif;font-weight:800;font-style:italic}
  .name-block{display:flex;flex-direction:column;align-items:flex-end}
  .candidate{font-family:"Open Sans",sans-serif;font-weight:800;letter-spacing:.01em;line-height:1;
    border-bottom:3px solid var(--white);padding-bottom:4px}
  .office{font-family:"Open Sans",sans-serif;font-weight:400;color:var(--white);margin-top:5px}

  .tagline{font-family:"Open Sans",sans-serif;font-style:italic}
  .tagline b{font-weight:800}
  .tagline span{font-weight:400}

  .platform{position:absolute;list-style:none;color:var(--white);font-family:"Open Sans",sans-serif;font-weight:800;font-style:italic}

  /* square sign */
  .sign--square .slogan{top:77px;font-size:58px}
  .sign--square .name-row{top:203px;gap:12px}
  .sign--square .elect{font-size:36px;margin-bottom:30px}
  .sign--square .candidate{font-size:60px}
  .sign--square .office{font-size:17px}
  .sign--square .tagline{top:324px;font-size:40px}
  .sign--square .web{top:411px;font-size:45px}
  .sign--square .platform{left:144px;top:482px;font-size:32px;line-height:45px}
  .sign--square .ballot{top:665px;font-size:72px}

  /* wide sign */
  .sign--wide .slogan{top:18px;font-size:32px}
  .sign--wide .name-row{top:95px;gap:8px}
  .sign--wide .elect{font-size:23px;margin-bottom:21px}
  .sign--wide .candidate{font-size:42px}
  .sign--wide .candidate.outlined{-webkit-text-stroke-width:3px}
  .sign--wide .office{font-size:11px;margin-top:3px}
  .sign--wide .tagline{top:184px;font-size:24px}
  .sign--wide .tagline.outlined{-webkit-text-stroke-width:3px}
  .sign--wide .web{top:235px;font-size:23px}
  .sign--wide .ballot{top:306px;font-size:38px}

  sup{font-size:.5em;vertical-align:.85em}
</style>
</head>
<body>
<main class="canvas">

  <section class="sign sign--square" aria-label="Square 4 by 4 foot sign">
    <h2 class="line slogan shadowed">Take back Our Town!</h2>
    <div class="line name-row">
      <span class="elect outlined">Elect</span>
      <div class="name-block">
        <h1 class="candidate outlined">DANA VELLOWAY</h1>
        <p class="office">for Brockmere Councilman / Trustee</p>
      </div>
    </div>
    <p class="line tagline outlined"><b>Fighting</b> <span>for</span> <b>Brockmere</b></p>
    <p class="line web shadowed">www.fairlevy.com</p>
    <ul class="platform shadowed">
      <li>- Stop HIGH taxes</li>
      <li>- Clean Up Our government</li>
      <li>- Preserve Our Neighborhoods</li>
    </ul>
    <p class="line ballot shadowed">Vote Nov. 8<sup>th</sup> “Row A”</p>
  </section>

  <section class="sign sign--wide" aria-label="36 by 24 inch sign">
    <h2 class="line slogan shadowed">Take back Our Town!</h2>
    <div class="line name-row">
      <span class="elect outlined">Elect</span>
      <div class="name-block">
        <h1 class="candidate outlined">DANA VELLOWAY</h1>
        <p class="office">for Brockmere Councilman / Trustee</p>
      </div>
    </div>
    <p class="line tagline outlined"><b>Fighting</b> <span>for</span> <b>Brockmere</b></p>
    <p class="line web shadowed">www.fairlevy.com</p>
    <p class="line ballot shadowed">Vote Nov. 8<sup>th</sup> “Row A”</p>
  </section>

</main>
</body>
</html>
```